Glass Recycling Company needs Logo and Business Card Design

Vorun Recycling needs a logo and business card design.
Vorun is a Cherokee word roughly translated as "together we go" but the company does not have any Cherokee affiliation. Concepts from the logo image can be incorporated but do not have to be. . The idea of community is integral to Vorun's identity as is environmental stewardship and social responsibility. Glass is infinitely recyclable, using the symbol for infinity would be cool.

Target Market(s)

Residential Customers

Industry/Entity Type

Glass Recycling

Contact Information for Business Card

Ned Bellham, Founder, cell: 555-318-4621, email: ned@vorunrecycling.example

Logo Text

Vorun Recycling, Tagline is Infinitely Better

Logo styles of interest
Abstract Logo
Font styles to use
Serif
Sans Serif
Other font styles liked:
• Any font that is easy to read from a distance, clear distinct letters

Colors
6B429C
8869AF
B7A5CE
E3DAEB
F3F0F8

Requirements
Must have
• Must us the name Vorun with a raised e with line under it. The idea behind that raised e is that when we go forward together we elevate everyone. Must use the color purple, purple is the industry standard for glass recycling. U
Nice to have
• Incorporate aspects from the traditional recycling logo
Should not have
• The old logo, although aspects could be used if appropriate

```html
<!DOCTYPE html>
<html lang="en">
<head>
<meta charset="utf-8">
<title>Vorun Recycling — Business Card</title>
<link rel="stylesheet" href="https://fonts.googleapis.com/css2?family=Arimo:wght@400;700&display=swap">
<style>
  :root {
    --purple: #633a7c;
    --purple-soft: #8869af;
    --white: #ffffff;
    --ink: #1d1d1f;
    --backdrop: #2b2b2d;
  }
  * { box-sizing: border-box; margin: 0; padding: 0; }
  html, body {
    width: 1200px; height: 1015px; overflow: hidden;
    background: var(--backdrop);
    font-family: "Arimo", Arial, sans-serif;
  }
  .stage {
    position: relative; width: 1200px; height: 1015px;
    display: flex; flex-direction: column; align-items: center; justify-content: center; gap: 60px;
  }
  .card {
    position: relative; width: 640px; height: 366px; overflow: hidden;
    box-shadow: 0 14px 30px rgba(0,0,0,.45);
  }
  .card--front {
    background: var(--purple);
    display: flex; align-items: center; justify-content: center;
  }
  .brand { color: var(--white); font-weight: 400; text-align: left; }
  .brand__name { display: block; font-size: 96px; line-height: 1; letter-spacing: 2px; }
  .brand__sub { display: block; font-size: 26px; letter-spacing: 22px; margin-top: 10px; padding-left: 4px; }

  .card--back { background: var(--white); }
  .back__tab {
    position: absolute; left: 0; top: 168px; width: 30px; height: 30px; background: var(--purple);
  }
  .back__mark { position: absolute; right: -120px; top: 40px; }
  .person { position: absolute; left: 52px; top: 128px; }
  .person__name { color: var(--purple); font-weight: 700; font-size: 24px; letter-spacing: .5px; }
  .person__role { color: var(--ink); font-size: 13px; letter-spacing: 1px; margin-top: 2px; }
  .contacts { position: absolute; left: 52px; top: 210px; list-style: none; }
  .contacts li {
    display: flex; align-items: center; gap: 8px;
    font-size: 15px; color: var(--ink); line-height: 22px;
  }
  .contacts svg { width: 13px; height: 13px; fill: var(--purple); flex: none; }
  .address {
    position: absolute; left: 60px; top: 296px; font-size: 15px; line-height: 20px; color: var(--ink);
  }
</style>
</head>
<body>
<main class="stage">
  <section class="card card--front" aria-label="Business card front">
    <div class="brand">
      <span class="brand__name">VORUN</span>
      <span class="brand__sub">RECYCLING</span>
    </div>
  </section>

  <section class="card card--back" aria-label="Business card back">
    <svg class="back__mark" width="380" height="380" viewBox="0 0 380 380" aria-hidden="true">
      <circle cx="190" cy="190" r="180" fill="var(--purple)"/>
    </svg>
    <span class="back__tab"></span>
    <div class="person">
      <p class="person__name">NED BELLHAM</p>
      <p class="person__role">FOUNDER</p>
    </div>
    <ul class="contacts">
      <li>
        <svg viewBox="0 0 24 24"><path d="M6.6 10.8a15 15 0 0 0 6.6 6.6l2.2-2.2c.3-.3.7-.4 1-.2 1.1.4 2.3.6 3.6.6.6 0 1 .4 1 1V20c0 .6-.4 1-1 1A17 17 0 0 1 3 4c0-.6.4-1 1-1h3.5c.6 0 1 .4 1 1 0 1.3.2 2.5.6 3.6.1.3 0 .7-.2 1z"/></svg>
        555-318-4621
      </li>
      <li>
        <svg viewBox="0 0 24 24"><path d="M2 5h20v14H2zm2 2v.5l8 5 8-5V7l-8 5z"/></svg>
        ned@vorunrecycling.example
      </li>
      <li>
        <svg viewBox="0 0 24 24"><path d="M12 2a10 10 0 1 0 0 20 10 10 0 0 0 0-20zm6.9 6h-3a15 15 0 0 0-1.3-3.9A8 8 0 0 1 18.9 8zM12 4c.8 1.2 1.5 2.5 1.9 4h-3.8c.4-1.5 1.1-2.8 1.9-4zM4.3 14a8 8 0 0 1 0-4h3.4a16 16 0 0 0 0 4zm.8 2h3a15 15 0 0 0 1.3 3.9A8 8 0 0 1 5.1 16zm3-8h-3a8 8 0 0 1 4.3-3.9C8.8 5.3 8.4 6.6 8.1 8zM12 20c-.8-1.2-1.5-2.5-1.9-4h3.8c-.4 1.5-1.1 2.8-1.9 4zm2.3-6H9.7a14 14 0 0 1 0-4h4.6a14 14 0 0 1 0 4zm.3 5.9c.6-1.2 1-2.5 1.3-3.9h3a8 8 0 0 1-4.3 3.9zm1.7-5.9a16 16 0 0 0 0-4h3.4a8 8 0 0 1 0 4z"/></svg>
        www.vorunrecycling.example
      </li>
    </ul>
    <p class="address">421, Address line goes here<br>45452, Country Name</p>
  </section>
</main>
</body>
</html>
```